Recruiting agency needs corporate presentation

We are a recruiting agency specialized in life sciences. We need a corporate presentation that will be sent to our clients and prospects in a PDF format.

Details of the presentation:
- a "brochure" type of presentation, VERTICAL, with 5 pages (please see "content" file attached) The presentation will be sent in a PDF format to our prospect clients by e-mail, so the choice of images and organization need to take that into account.
- In the attachment, you will find our logo "Harlow & Associates".
- the presentation needs to convey our industry (life sciences, healthcare) and a high level of professionalism/leadership We want a sophisticated and elegant brochure.
- page 2 of the brochure needs to contain all the logos attached, in a very elegant, clear and organized way.
- page 3 shows a map with cursors (please see content file). The following countries/continents on the map need to be highlighted: USA, Brazil, Europe, North Africa, South Africa, China. We need "cursors" like pins to show where on the map our offices are: Miami, Boston, Lausanne, Denmark, Paris, Copenhaguen.
- page 4 includes pie charts (please see "Statistics 2020" Excel file): please improve the pie charts aesthetics, it needs to look very modern.

Target Market(s)

Healthcare / Life Sciences.

Requirements
Must have
• Very modern and aesthetics. I included a presentation of companies that we like to give you an indication of the overall style we're looking for.

```html
<!DOCTYPE html>
<html lang="en">
<head>
<meta charset="utf-8">
<title>Harlow &amp; Associates – Corporate Brochure</title>
<link rel="stylesheet" href="https://fonts.googleapis.com/css2?family=Roboto+Condensed:wght@400;700&display=swap">
<style>
  :root {
    --stage: #ece9e4;
    --paper: #f7f7f7;
    --paper-shade: #e4e4e4;
    --ink: #1c1c1c;
    --ink-soft: #3a3a3a;
    --gold: #c9a021;
    --yellow: #f6c533;
    --rule: #2a2a2a;
    --lab-dark: #0c1f2e;
    --lab-green: #5fae3a;
    --lab-blue: #1c5c86;
  }
  * { margin: 0; padding: 0; box-sizing: border-box; }
  html, body { width: 1200px; height: 907px; overflow: hidden; }
  body {
    background: var(--stage);
    font-family: "Roboto Condensed", "Arial Narrow", sans-serif;
    color: var(--ink);
  }
  .spread {
    position: relative;
    width: 1200px;
    height: 907px;
    display: flex;
    justify-content: center;
    align-items: center;
    gap: 40px;
  }
  .page {
    position: relative;
    width: 340px;
    height: 480px;
    background: linear-gradient(100deg, var(--paper) 40%, var(--paper-shade) 100%);
    overflow: hidden;
    box-shadow: 0 6px 18px rgba(0,0,0,0.18);
  }

  /* footer */
  .page-footer {
    position: absolute;
    left: 14px; right: 0; bottom: 18px;
    display: flex; align-items: center; gap: 6px;
    font-size: 5.5px; color: var(--ink-soft);
  }
  .page-footer::after {
    content: ""; flex: 1; height: 1px; background: var(--rule);
  }

  /* cover */
  .brand-name {
    position: absolute; top: 60px; right: 22px;
    font-size: 10px; font-weight: 400; color: var(--ink);
  }
  .cover-visual {
    position: absolute; left: 0; right: 0; top: 152px; height: 198px;
    background:
      radial-gradient(circle at 32% 38%, rgba(170,230,90,0.85) 0 6%, rgba(95,174,58,0.45) 16%, transparent 34%),
      radial-gradient(circle at 62% 62%, rgba(60,140,220,0.55), transparent 30%),
      linear-gradient(120deg, var(--lab-dark) 0%, var(--lab-blue) 55%, var(--lab-dark) 100%);
  }
  .cover-title { position: absolute; left: 16px; top: 362px; }
  .cover-title .lead { font-size: 18px; font-weight: 700; line-height: 1.1; }
  .cover-title .focus { font-size: 30px; font-weight: 700; color: var(--gold); line-height: 1.05; }
  .cover-title .sub { font-size: 7px; margin-top: 4px; color: var(--ink-soft); }

  /* inner pages */
  .page-num {
    position: absolute; top: 22px; left: 18px; right: 12px;
    display: flex; align-items: center; gap: 6px;
  }
  .page-num span {
    width: 11px; height: 11px; background: var(--gold); color: #fff;
    font-size: 8px; font-weight: 700; line-height: 11px; text-align: center;
  }
  .page-num::after { content: ""; flex: 1; height: 1px; background: var(--rule); }
  .section-title {
    position: absolute; left: 20px; top: 62px;
    font-size: 29px; font-weight: 700; line-height: 1.05;
  }
  .section-rule {
    position: absolute; left: 97px; top: 120px; width: 210px; height: 2px;
  }
  .section-copy p { font-size: 7px; font-weight: 400; line-height: 1.4; color: var(--ink-soft); }
  .section-copy p + p { margin-top: 8px; }

  .about--classic .section-title { color: var(--gold); }
  .about--classic .section-rule { background: var(--gold); }
  .about--classic .section-copy { position: absolute; left: 25px; top: 165px; width: 152px; }
  .about--classic .about-visual {
    position: absolute; left: 88px; top: 262px; width: 252px; height: 180px;
    background: linear-gradient(110deg, #3a3a3a 0%, #9a9a9a 45%, #d8d8d8 70%, #5a5a5a 100%);
  }

  .about--accent .section-title { color: var(--ink); }
  .about--accent .section-rule { background: var(--ink); }
  .about--accent .about-visual {
    position: absolute; left: 85px; top: 262px; width: 255px; height: 165px;
    background: linear-gradient(110deg, #4c6e86 0%, #a9c0cf 40%, #e2ebf0 65%, #6a8296 100%);
  }
  .about--accent .accent-block {
    position: absolute; left: 0; top: 134px; width: 200px; height: 186px;
    background: var(--yellow); opacity: 0.88;
  }
  .about--accent .section-copy { position: absolute; left: 22px; top: 150px; width: 152px; }
  .about--accent .section-copy p { color: var(--ink); }
</style>
</head>
<body>
<main class="spread">

  <section class="page cover">
    <div class="brand-name">Harlow &amp; Associates</div>
    <div class="cover-visual" role="img" aria-label="Gloved hand holding a glowing green test tube over a chemical structure network"></div>
    <div class="cover-title">
      <div class="lead">Best Recruiters in</div>
      <div class="focus">Life Sciences</div>
      <div class="sub">Finding the best talents in USA and Europe</div>
    </div>
    <footer class="page-footer">www.harlowassociates.com</footer>
  </section>

  <section class="page about about--classic">
    <div class="page-num"><span>1</span></div>
    <h2 class="section-title">About<br>Us</h2>
    <div class="section-rule"></div>
    <div class="section-copy">
      <p>We are an international recruiting boutique agency specialized in Life Sciences. In the last 3 decades, we have appointed thousands of professionalsglobally.</p>
      <p>Our firm is known for being highly committed and able to deliver great results within budget and timing constraints.Equality and parity are at the core of our activity.</p>
    </div>
    <div class="about-visual" role="img" aria-label="Black and white photo of scientists working with microscopes in a laboratory"></div>
    <footer class="page-footer">www.harlowassociates.com</footer>
  </section>

  <section class="page about about--accent">
    <div class="page-num"><span>1</span></div>
    <h2 class="section-title">About<br>Us</h2>
    <div class="section-rule"></div>
    <div class="about-visual" role="img" aria-label="Colour photo of scientists working with microscopes in a laboratory"></div>
    <div class="accent-block"></div>
    <div class="section-copy">
      <p>We are an international recruiting boutique agency specialized in Life Sciences. In the last 3 decades, we have appointed thousands of professionalsglobally.</p>
      <p>Our firm is known for being highly committed and able to deliver great results within budget and timing constraints.Equality and parity are at the core of our activity.</p>
    </div>
    <footer class="page-footer">www.harlowassociates.com</footer>
  </section>

</main>
</body>
</html>
```